Tall Willow Sticker Design for TRIM 9

ur business name is ' Tall Willow ' ( Logo attached ).
The Product is called ' Trim 9 ' It has six ingredients that need to be listed on the sticker - Chia, Turmeric, Ginger, Dandelion, Macha and Seaweed.
120 capsules in a packet.
I would like it to say the product is a ' Weight loss alternative ' ' all organic ingredients ' All natural '

The logo.

Target Market(s)

Everyone.

Industry/Entity Type

Health And Wellness

Requirements
Must have
• ur business name is ' Tall Willow ' ( Logo attached ).
• The Product is called ' Trim 9 ' It has six ingredients that need to be listed on the sticker - Chia, Turmeric, Ginger, Dandelion, Macha and Seaweed.
• 120 capsules in a packet.
• I would like it to say the product is a ' Weight loss alternative ' ' all organic ingredients ' All natural '
• The logo.
Nice to have
• A catchy image symbolising nature.

```html
<!DOCTYPE html>
<html lang="en">
<head>
<meta charset="utf-8">
<title>Tall Willow – Trim 9 Sticker</title>
<link rel="stylesheet" href="https://fonts.googleapis.com/css2?family=Lobster+Two:ital,wght@1,700&family=Marcellus&family=Open+Sans:ital,wght@0,400;0,800;1,800&display=swap">
<style>
  :root {
    --bg: #ffffff;
    --gold-light: #f6ecc4;
    --gold: #d7c286;
    --gold-dark: #a88f4e;
    --green-dark: #1f6b22;
    --green: #3d9a2f;
    --green-light: #7cc24a;
    --leaf-pale: #dff0d6;
    --black: #121212;
    --white: #ffffff;
    --capsule: #e2d6a8;
  }
  html, body {
    margin: 0;
    padding: 0;
    width: 1200px;
    height: 960px;
    overflow: hidden;
    background: var(--bg);
  }
  .canvas {
    width: 1200px;
    height: 960px;
    position: relative;
  }
  .sticker {
    position: absolute;
    left: 180px;
    top: 60px;
    width: 840px;
    height: 840px;
  }
  .band-text {
    font-family: "Lobster Two", cursive;
    font-style: italic;
    font-weight: 700;
  }
  .ingredients { font-size: 30px; fill: var(--white); }
  .claim { font-size: 46px; fill: var(--gold); }
  .brand-name {
    font-family: "Marcellus", serif;
    font-size: 48px;
    fill: var(--green-light);
  }
  .product-name {
    font-family: "Open Sans", sans-serif;
    font-weight: 800;
    font-size: 78px;
    fill: var(--white);
  }
  .dose {
    font-family: "Open Sans", sans-serif;
    font-style: italic;
    font-weight: 800;
    font-size: 34px;
    fill: var(--gold-light);
  }
  .count {
    font-family: "Open Sans", sans-serif;
    font-size: 18px;
    fill: var(--white);
  }
</style>
</head>
<body>
<main class="canvas">
  <svg class="sticker" viewBox="0 0 840 840" xmlns="http://www.w3.org/2000/svg" aria-label="Trim 9 round sticker">
    <defs>
      <linearGradient id="gold-ring" x1="0" y1="0" x2="1" y2="1">
        <stop offset="0" stop-color="var(--gold-light)"/>
        <stop offset="0.5" stop-color="var(--gold)"/>
        <stop offset="1" stop-color="var(--gold-dark)"/>
      </linearGradient>
      <linearGradient id="green-band" x1="0" y1="0" x2="1" y2="1">
        <stop offset="0" stop-color="var(--green-light)"/>
        <stop offset="0.5" stop-color="var(--green)"/>
        <stop offset="1" stop-color="var(--green-dark)"/>
      </linearGradient>
      <radialGradient id="leaf-scene" cx="0.4" cy="0.4" r="0.7">
        <stop offset="0" stop-color="var(--leaf-pale)"/>
        <stop offset="0.6" stop-color="var(--green-light)"/>
        <stop offset="1" stop-color="var(--green-dark)"/>
      </radialGradient>
      <path id="arc-top" d="M 95,420 A 325 325 0 0 1 745,420"/>
      <path id="arc-bottom" d="M 55,420 A 365 365 0 0 0 785,420"/>
    </defs>

    <g class="outer-rings">
      <circle cx="420" cy="420" r="418" fill="url(#gold-ring)"/>
      <circle cx="420" cy="420" r="404" fill="url(#green-band)"/>
    </g>

    <text class="band-text ingredients">
      <textPath href="#arc-top" startOffset="50%" text-anchor="middle">Ingredients: Chia, Turmeric, Ginger, Dandelion, Macha and Seaweed.</textPath>
    </text>
    <text class="band-text claim">
      <textPath href="#arc-bottom" startOffset="50%" text-anchor="middle" dominant-baseline="hanging">Weight Loss Alternative and All Natural Ingredients.</textPath>
    </text>

    <g class="inner-rings">
      <circle cx="420" cy="420" r="292" fill="url(#gold-ring)"/>
      <circle cx="420" cy="420" r="278" fill="url(#leaf-scene)" role="img" aria-label="Close-up photograph of fresh green leaves"/>
    </g>

    <g class="label-core">
      <circle cx="420" cy="400" r="178" fill="var(--black)" stroke="var(--gold-light)" stroke-width="3"/>
      <text class="brand-name" x="420" y="322" text-anchor="middle">Tall Willow</text>
      <text class="product-name" x="420" y="440" text-anchor="middle">Trim 9</text>
      <text class="dose" x="420" y="492" text-anchor="middle">1000mg</text>
      <text class="count" x="420" y="530" text-anchor="middle">120 Capsules</text>
    </g>

    <ellipse cx="420" cy="608" rx="72" ry="30" fill="var(--capsule)" role="img" aria-label="Illustration of two herbal capsules on green leaves"/>
  </svg>
</main>
</body>
</html>
```